RTV CRAFTED

building services
decks
pergola
renovation
extensions
general building

Target Market(s)

middle to upper class

Industry/Entity Type

building

Contact Information for Business Card

my details 0427839152 pkharlow47@mailvane.net BLD574926

Font styles to use
Serif

Colors
00AB8E
00BBA5
67D7C9
C6EFE9
E9F9F6

Requirements
Must have
• logo on the front and details on the back
Nice to have
• sharp and clean lines

```html
<!DOCTYPE html>
<html lang="en">
<head>
<meta charset="utf-8">
<title>RTV Crafted Business Card</title>
<link rel="stylesheet" href="https://fonts.googleapis.com/css2?family=Karla:wght@400;500;700&display=swap">
<style>
  :root {
    --backdrop: #9b9b9b;
    --card-light: #ffffff;
    --card-dark: #353335;
    --brand-green: #03b873;
    --ink: #111111;
    --logo-light: #d6d6d6;
    --band-text: #ffffff;
  }
  * { margin: 0; padding: 0; box-sizing: border-box; }
  html, body {
    width: 1133px; height: 1200px; overflow: hidden;
    background: var(--backdrop);
    font-family: "Karla", Arial, sans-serif;
  }
  .canvas { position: relative; width: 1133px; height: 1200px; }
  .card {
    position: absolute; left: 196px; width: 734px; height: 418px;
  }
  .card--front { top: 139px; background: var(--card-light); }
  .card--back { top: 641px; background: var(--card-dark); }

  .wordmark {
    position: absolute; left: 0; right: 0; text-align: center;
    font-weight: 700; font-size: 62px; letter-spacing: 1px; line-height: 1;
  }
  .card--front .wordmark { top: 118px; color: var(--ink); }
  .card--back .wordmark { top: 170px; color: var(--logo-light); }

  .band { position: absolute; left: 0; overflow: visible; }
  .band--front { top: 297px; width: 706px; height: 80px; }
  .band--back { top: 347px; width: 684px; height: 34px; }
  .band polygon { fill: var(--brand-green); }

  .band-content {
    position: absolute; color: var(--band-text);
  }
  .holder { left: 49px; top: 316px; }
  .holder-name { font-size: 22px; font-weight: 700; letter-spacing: 1.2px; line-height: 1.1; }
  .holder-role { font-size: 16px; letter-spacing: 0.8px; margin-top: 2px; }

  .divider {
    position: absolute; top: 318px; width: 1px; height: 34px; background: var(--band-text);
  }
  .divider--one { left: 272px; }
  .divider--two { left: 528px; }

  .contact { left: 300px; top: 313px; font-size: 16px; letter-spacing: 0.4px; line-height: 22px; }
  .contact-row { display: flex; align-items: center; gap: 8px; }
  .contact-row svg { width: 14px; height: 14px; fill: var(--band-text); }

  .licence { left: 559px; top: 327px; font-size: 16px; letter-spacing: 0.8px; }

  .services {
    left: 42px; top: 353px; font-size: 15px; letter-spacing: 0.2px;
    display: flex; align-items: center; white-space: nowrap;
  }
  .services svg { width: 11px; height: 11px; margin: 0 3px; }
</style>
</head>
<body>
<div class="canvas">

  <section class="card card--front">
    <div class="wordmark">RTV CRAFTED</div>

    <svg class="band band--front" viewBox="0 0 706 80" aria-hidden="true">
      <polygon points="0,0 685,0 706,40 685,80 0,80"/>
    </svg>

    <div class="band-content holder">
      <div class="holder-name">OWEN PRESCOTT</div>
      <div class="holder-role">President</div>
    </div>
    <div class="divider divider--one"></div>

    <div class="band-content contact">
      <div class="contact-row">
        <svg viewBox="0 0 24 24" aria-hidden="true"><path d="M6.6 10.8c1.4 2.8 3.8 5.1 6.6 6.6l2.2-2.2c.3-.3.7-.4 1-.2 1.1.4 2.3.6 3.6.6.6 0 1 .4 1 1V20c0 .6-.4 1-1 1C10.6 21 3 13.4 3 4c0-.6.4-1 1-1h3.5c.6 0 1 .4 1 1 0 1.3.2 2.5.6 3.6.1.3 0 .7-.2 1z"/></svg>
        <span>042-783-9152</span>
      </div>
      <div class="contact-row">
        <svg viewBox="0 0 24 24" aria-hidden="true"><path d="M2 5h20v14H2z M3 6l9 7 9-7" stroke="#03b873" stroke-width="1.6"/></svg>
        <span>pkharlow47@mailvane.net</span>
      </div>
    </div>
    <div class="divider divider--two"></div>

    <div class="band-content licence">BLD574926</div>
  </section>

  <section class="card card--back">
    <div class="wordmark">RTV CRAFTED</div>

    <svg class="band band--back" viewBox="0 0 684 34" aria-hidden="true">
      <polygon points="0,0 671,0 684,17 671,34 0,34"/>
    </svg>

    <div class="band-content services">
      <span>Building Services</span>
      <svg viewBox="0 0 12 12" aria-hidden="true"><rect x="0.7" y="0.7" width="10.6" height="10.6" fill="none" stroke="#fff" stroke-width="1.4"/><path d="M3 6l2 2 4-4" fill="none" stroke="#fff" stroke-width="1.5"/></svg>
      <span>Decks</span>
      <svg viewBox="0 0 12 12" aria-hidden="true"><rect x="0.7" y="0.7" width="10.6" height="10.6" fill="none" stroke="#fff" stroke-width="1.4"/><path d="M3 6l2 2 4-4" fill="none" stroke="#fff" stroke-width="1.5"/></svg>
      <span>Pergola</span>
      <svg viewBox="0 0 12 12" aria-hidden="true"><rect x="0.7" y="0.7" width="10.6" height="10.6" fill="none" stroke="#fff" stroke-width="1.4"/><path d="M3 6l2 2 4-4" fill="none" stroke="#fff" stroke-width="1.5"/></svg>
      <span>Renovation</span>
      <svg viewBox="0 0 12 12" aria-hidden="true"><rect x="0.7" y="0.7" width="10.6" height="10.6" fill="none" stroke="#fff" stroke-width="1.4"/><path d="M3 6l2 2 4-4" fill="none" stroke="#fff" stroke-width="1.5"/></svg>
      <span>Extensions</span>
      <svg viewBox="0 0 12 12" aria-hidden="true"><rect x="0.7" y="0.7" width="10.6" height="10.6" fill="none" stroke="#fff" stroke-width="1.4"/><path d="M3 6l2 2 4-4" fill="none" stroke="#fff" stroke-width="1.5"/></svg>
      <span>General Building</span>
    </div>
  </section>

</div>
</body>
</html>
```